Business card design needed

Hi,
I was hoping to have a business card designed with a background similar to dark coloured concrete texture. I have a photo of the particular concrete that I would like to be used as the background but for some reason it wouldn't let me upload the image. Please email me for the image and I will send to you asap.
I would like the company name to be in a font that is thin, crisp to reflect 'precision'. I am trying to convey that my services are more precise and have more attention to detail than my competitors. I would like this to be represented through the font if possible.
Colours are at your discretion - although we would like it to attract the eye and stand out. We would like the card to be in a modern style.
I was thinking for an image in the background of the card, or on the side of the card wherever is appropriate, half of a ring saw blade or similar.
The company is a concrete cutting and drilling service - we are a 24 hour 7 day service which is unique to the industry. We provide a more detailed service to our customers and this is the backbone of our reputation.
Target Market(s)
Construction industry & general public
Industry/Entity Type
Concrete
Contact Information for Business Card
Ember Ridge Trenching Pty Ltd
Concrete Cutting & Drilling
24 hour 7 day service
Douglas Whitfield
Director
M: 0492 518 307
P: (07) 3196 4052
E: emberridgetrench@mailvista.net
PO Box 816, Tallowood DC QLD 4173

```html
<!DOCTYPE html>
<html lang="en">
<head>
<meta charset="utf-8">
<title>Ember Ridge Trenching – Business Card</title>
<link href="https://fonts.googleapis.com/css2?family=Stardos+Stencil:wght@400;700&family=Saira+Condensed:wght@400;500&family=Open+Sans:ital,wght@0,400;1,400&display=swap" rel="stylesheet">
<style>
  :root {
    --backdrop: #3a3430;
    --concrete-light: #a5a891;
    --concrete-mid: #8f937b;
    --concrete-dark: #5f6352;
    --band-fill: #c8cccd;
    --band-edge: #8a8f90;
    --ink: #1c1d1a;
    --ink-soft: #2a2c26;
    --chalk: #eef0ea;
  }
  html, body {
    margin: 0;
    width: 1200px;
    height: 900px;
    overflow: hidden;
    background: var(--backdrop);
  }
  .card {
    position: absolute;
    left: 100px;
    top: 145px;
    width: 1000px;
    height: 610px;
    overflow: hidden;
    box-shadow: 0 18px 40px rgba(0,0,0,.45);
  }
  .concrete-texture {
    position: absolute;
    inset: 0;
    background:
      radial-gradient(ellipse at 55% 45%, var(--concrete-light) 0%, var(--concrete-mid) 55%, var(--concrete-dark) 100%);
  }
  .holder {
    position: absolute;
    left: 70px;
    top: 110px;
    font-family: "Open Sans", sans-serif;
    color: var(--chalk);
  }
  .holder-name {
    font-size: 26px;
    letter-spacing: 3px;
    text-transform: uppercase;
    margin: 0;
  }
  .holder-role {
    font-size: 24px;
    font-style: italic;
    margin: 0;
    opacity: .9;
  }
  .service {
    position: absolute;
    left: 590px;
    top: 70px;
    transform: rotate(-8deg);
    transform-origin: left top;
    color: var(--ink);
  }
  .service-main {
    font-family: "Stardos Stencil", serif;
    font-weight: 700;
    font-size: 58px;
    letter-spacing: 4px;
    line-height: 1;
    margin: 0;
  }
  .service-sub {
    font-family: "Stardos Stencil", serif;
    font-size: 24px;
    letter-spacing: 2px;
    margin: 2px 0 0;
  }
  .service-hours {
    font-family: "Saira Condensed", sans-serif;
    font-size: 22px;
    margin: 0 0 0 150px;
    letter-spacing: 1px;
  }
  .service-hours strong {
    font-size: 30px;
    font-weight: 500;
  }
  .name-band {
    position: absolute;
    left: 0;
    top: 0;
  }
  .company-name {
    font-family: "Stardos Stencil", serif;
    font-weight: 700;
    font-size: 36px;
    fill: var(--ink);
  }
  .contact {
    position: absolute;
    left: 90px;
    top: 470px;
    transform: rotate(-20deg);
    transform-origin: left top;
    font-family: "Saira Condensed", sans-serif;
    font-size: 22px;
    line-height: 1.35;
    letter-spacing: 1.5px;
    text-transform: uppercase;
    font-style: normal;
    color: var(--ink-soft);
    margin: 0;
  }
</style>
</head>
<body>
  <div class="card">
    <div class="concrete-texture" role="img" aria-label="Dark green-grey cracked concrete texture"></div>

    <div class="holder">
      <p class="holder-name">Douglas Whitfield</p>
      <p class="holder-role">Director</p>
    </div>

    <div class="service">
      <p class="service-main">CONCRETE</p>
      <p class="service-sub">CUTTING &amp; DRILLING</p>
      <p class="service-hours"><strong>24/7</strong> HOURS SERVICE</p>
    </div>

    <svg class="name-band" width="1000" height="610" viewBox="0 0 1000 610">
      <polygon fill="var(--band-edge)"
        points="90,305 150,292 330,270 430,268 470,255 510,258 560,240 610,246 650,236 700,232 760,244 850,226 880,282 640,318 520,330 470,326 400,348 260,362 100,368 80,340" />
      <polygon fill="var(--band-fill)"
        points="96,310 152,298 332,276 432,274 472,262 512,264 562,247 612,252 652,243 702,239 760,250 844,233 872,284 640,314 520,326 470,322 400,343 260,357 104,362 86,340" />
      <text class="company-name" x="120" y="350"
        transform="rotate(-5.8 120 350)"
        textLength="720" lengthAdjust="spacingAndGlyphs">EMBER RIDGE TRENCHING PTY LTD</text>
    </svg>

    <address class="contact">
      PO Box 816, Tallowood DC QLD 4173<br>
      M: 0492 518 307<br>
      P: (07) 3196 4052<br>
      E: emberridgetrench@mailvista.net
    </address>
  </div>
</body>
</html>
```